Retractable Banner Design for Retail Shopping Event

I need a design for a 33” by 86” retractable banner. It should have my logo at the top (the largest element of the design) and the banner should also include my website and Instagram handle:
www.verikamode.com
@verikamode
I have included product pictures in the brief that can be used. I also included different versions of my logo file, including AI. I need the file to be ready to upload to my printer.
My store is an upscale women’s boutique. I am also attaching designs I have selected in the past to give an idea of my aesthetic.

```html
<!DOCTYPE html>
<html lang="en">
<head>
<meta charset="utf-8">
<title>Verikamode – Ship &amp; Shop Banner</title>
<link href="https://fonts.googleapis.com/css2?family=Playfair+Display:wght@700&family=Roboto+Condensed:wght@400&family=Roboto:wght@400;500&display=swap" rel="stylesheet">
<style>
  :root {
    --blush: #efcfc7;
    --ink: #5f5c5b;
    --ink-soft: #676363;
    --tile-light: #fbfaf8;
    --tile-mid: #ece6df;
    --leopard: #c9a678;
    --slipper: #b9a8b4;
    --tote: #cdb7a1;
  }
  * { margin: 0; padding: 0; box-sizing: border-box; }
  html, body { width: 1200px; height: 3124px; overflow: hidden; }
  body { background: var(--blush); font-family: "Roboto", sans-serif; color: var(--ink); }
  .banner { position: relative; width: 1200px; height: 3124px; }
  .brand-name {
    position: absolute; top: 250px; left: 0; width: 1200px;
    text-align: center; font-family: "Playfair Display", serif; font-weight: 700;
    font-size: 128px; letter-spacing: 6px; color: var(--ink);
  }
  .headline {
    position: absolute; top: 635px; left: 0; width: 1200px; text-align: center;
    font-family: "Playfair Display", serif; font-weight: 700; font-size: 104px;
    letter-spacing: 2px; color: var(--ink);
  }
  .tagline {
    position: absolute; top: 795px; left: 0; width: 1200px; text-align: center;
    font-family: "Roboto Condensed", sans-serif; font-size: 54px; color: var(--ink);
  }
  .product {
    position: absolute; width: 440px; height: 448px;
  }
  .product--earrings { left: 140px; top: 940px; background: radial-gradient(circle, #e8d39a 0%, var(--tile-light) 45%); }
  .product--tray { left: 632px; top: 940px; background: radial-gradient(circle, var(--leopard) 0%, #a7845a 48%, var(--tile-light) 52%); }
  .product--slippers { left: 140px; top: 1440px; background: radial-gradient(ellipse at 50% 55%, #efe3dc 0%, var(--slipper) 40%, var(--tile-light) 62%); }
  .product--tote { left: 632px; top: 1440px; background: linear-gradient(180deg, var(--tile-mid) 0%, var(--tote) 40%, var(--tote) 90%, var(--tile-mid) 100%); }
  .invite {
    position: absolute; top: 1955px; left: 0; width: 1200px; text-align: center;
    font-size: 68px; line-height: 84px; color: var(--ink-soft);
  }
  .handle {
    position: absolute; top: 2650px; left: 0; width: 1200px; text-align: center;
    font-size: 64px; color: var(--ink-soft);
  }
  .phone {
    position: absolute; top: 2815px; left: 0; width: 1200px; text-align: center;
    font-size: 70px; font-weight: 500; letter-spacing: 2px; color: var(--ink);
  }
  .contact-line {
    position: absolute; top: 2950px; left: 0; width: 1200px; text-align: center;
    font-size: 50px; color: var(--ink-soft);
  }
  .contact-line .divider { margin: 0 22px; }
</style>
</head>
<body>
<main class="banner">
  <div class="brand-name">VERIKAMODE</div>
  <h1 class="headline">SHIP &amp; SHOP</h1>
  <p class="tagline">Make Your Life Beautiful</p>

  <div class="product product--earrings" role="img" aria-label="Gold flower stud earrings with crystal centers"></div>
  <div class="product product--tray" role="img" aria-label="Round leopard print lacquer tray"></div>
  <div class="product product--slippers" role="img" aria-label="Lilac slippers with blush pom-poms"></div>
  <div class="product product--tote" role="img" aria-label="Beige tote bag with a teal graphic"></div>

  <p class="invite">Be the first to preview<br>our new winter collection and<br>get an early start<br>on your holiday gifting</p>

  <p class="handle">@verikamode</p>
  <p class="phone">(555) 014-2867</p>
  <p class="contact-line">info@verikamode.com<span class="divider">|</span>www.verikamode.com</p>
</main>
</body>
</html>
```